Crestfield Automotive Business Card

Automotive repair , all makes including Asian and European Imports. QMR Certified (Logo),Chatterbook (logo), Pingly+ (logo)

Industry/Entity Type

Automotive

Contact Information for Business Card

Crestfield Automotive, Ray Hobart Owner, 3817 Larch Ave. Worthington, Mn 58402. Website crestfieldautomotive.example. (555) 641-0938

```html
<!DOCTYPE html>
<html lang="en">
<head>
<meta charset="utf-8">
<title>Crestfield Automotive Business Card</title>
<link href="https://fonts.googleapis.com/css2?family=Oswald:wght@700&family=Exo+2:wght@300;400;500&display=swap" rel="stylesheet">
<style>
  :root {
    --page-bg: #e9e7e3;
    --card-white: #ffffff;
    --brand-blue: #1534a0;
    --brand-blue-deep: #0a2481;
    --brand-blue-light: #2a4fc4;
    --brand-red: #e2283a;
    --brand-red-dark: #b81628;
    --ink-dark: #2a2a2a;
    --ink-soft: #555555;
    --text-light: #ffffff;
  }
  * { margin: 0; padding: 0; box-sizing: border-box; }
  html, body {
    width: 1200px;
    height: 828px;
    overflow: hidden;
    background: var(--page-bg);
  }
  .canvas {
    position: relative;
    width: 1200px;
    height: 828px;
  }
  .card {
    position: absolute;
    left: 285px;
    width: 630px;
    height: 360px;
    background: var(--card-white);
    overflow: hidden;
    box-shadow: 0 6px 18px rgba(0,0,0,0.18);
  }
  .card--front { top: 36px; }
  .card--back { top: 432px; }
  .card__wave {
    position: absolute;
    inset: 0;
    width: 100%;
    height: 100%;
  }
  .brand {
    position: absolute;
    display: flex;
    align-items: center;
    gap: 10px;
    white-space: nowrap;
  }
  .brand__mark {
    width: 14px;
    height: 14px;
    background: var(--brand-red);
  }
  .brand__name {
    font-family: "Oswald", sans-serif;
    font-weight: 700;
    color: var(--brand-blue);
    text-transform: uppercase;
    letter-spacing: 1px;
    line-height: 1;
  }
  .card--front .brand { right: 52px; top: 34px; }
  .card--front .brand__name { font-size: 30px; }
  .card--back .brand { left: 40px; top: 84px; }
  .card--back .brand__name { font-size: 28px; }

  .person {
    position: absolute;
    right: 40px;
    top: 36px;
    text-align: right;
    font-family: "Exo 2", sans-serif;
  }
  .person__name {
    font-size: 22px;
    font-weight: 400;
    color: var(--ink-dark);
    letter-spacing: 1.5px;
  }
  .person__title {
    font-size: 10px;
    font-weight: 500;
    color: var(--ink-soft);
    letter-spacing: 2px;
    text-transform: uppercase;
    margin-top: 2px;
  }
  .address {
    position: absolute;
    right: 40px;
    top: 170px;
    text-align: right;
    font-family: "Exo 2", sans-serif;
    font-size: 16px;
    font-weight: 400;
    color: var(--text-light);
    line-height: 1.35;
    letter-spacing: 0.5px;
  }
  .contacts {
    position: absolute;
    left: 40px;
    bottom: 28px;
    list-style: none;
    font-family: "Exo 2", sans-serif;
    font-size: 13px;
    font-weight: 400;
    color: var(--text-light);
    letter-spacing: 0.4px;
  }
  .contacts__item {
    display: flex;
    align-items: center;
    gap: 10px;
    height: 22px;
  }
  .contacts__icon {
    width: 13px;
    height: 13px;
    flex: none;
  }
</style>
</head>
<body>
<main class="canvas">

  <section class="card card--front" aria-label="Business card front">
    <svg class="card__wave" viewBox="0 0 630 360" preserveAspectRatio="none" aria-hidden="true">
      <defs>
        <linearGradient id="blueFieldFront" x1="0" y1="0" x2="1" y2="1">
          <stop offset="0" stop-color="var(--brand-blue-light)"/>
          <stop offset="0.6" stop-color="var(--brand-blue)"/>
          <stop offset="1" stop-color="var(--brand-blue-deep)"/>
        </linearGradient>
        <linearGradient id="redBandFront" x1="0" y1="0" x2="0" y2="1">
          <stop offset="0" stop-color="var(--brand-red)"/>
          <stop offset="1" stop-color="var(--brand-red-dark)"/>
        </linearGradient>
      </defs>
      <path d="M0,268 C170,250 290,225 370,165 C450,105 540,92 630,86 L630,360 L0,360 Z" fill="url(#redBandFront)"/>
      <path d="M0,290 C185,272 305,245 388,185 C470,126 552,114 630,110 L630,360 L0,360 Z" fill="url(#blueFieldFront)"/>
    </svg>
    <div class="brand">
      <span class="brand__mark" aria-hidden="true"></span>
      <span class="brand__name">Crestfield Automotive</span>
    </div>
  </section>

  <section class="card card--back" aria-label="Business card back">
    <svg class="card__wave" viewBox="0 0 630 360" preserveAspectRatio="none" aria-hidden="true">
      <defs>
        <linearGradient id="blueFieldBack" x1="0" y1="0" x2="1" y2="1">
          <stop offset="0" stop-color="var(--brand-blue-light)"/>
          <stop offset="0.6" stop-color="var(--brand-blue)"/>
          <stop offset="1" stop-color="var(--brand-blue-deep)"/>
        </linearGradient>
        <linearGradient id="redBandBack" x1="0" y1="0" x2="0" y2="1">
          <stop offset="0" stop-color="var(--brand-red)"/>
          <stop offset="1" stop-color="var(--brand-red-dark)"/>
        </linearGradient>
      </defs>
      <path d="M0,222 C170,212 300,195 385,145 C465,98 545,80 630,74 L630,360 L0,360 Z" fill="url(#redBandBack)"/>
      <path d="M0,244 C185,234 315,215 402,165 C484,118 556,102 630,100 L630,360 L0,360 Z" fill="url(#blueFieldBack)"/>
    </svg>

    <div class="person">
      <p class="person__name">RAY HOBART</p>
      <p class="person__title">Owner</p>
    </div>

    <div class="brand">
      <span class="brand__mark" aria-hidden="true"></span>
      <span class="brand__name">Crestfield Automotive</span>
    </div>

    <p class="address">3817 Larch Ave.<br>Worthington, MN 58402</p>

    <ul class="contacts">
      <li class="contacts__item">
        <svg class="contacts__icon" viewBox="0 0 16 16" aria-hidden="true"><path d="M3 1h3l1.5 4-2 1.2a9 9 0 0 0 4.3 4.3L11 8.5l4 1.5v3a2 2 0 0 1-2 2A12 12 0 0 1 1 3a2 2 0 0 1 2-2z" fill="#fff"/></svg>
        <span>(555) 641-0938</span>
      </li>
      <li class="contacts__item">
        <svg class="contacts__icon" viewBox="0 0 16 16" aria-hidden="true"><rect x="4" y="1" width="8" height="14" rx="1.5" fill="none" stroke="#fff" stroke-width="1.6"/><circle cx="8" cy="12.5" r="0.9" fill="#fff"/></svg>
        <span>(555) 641-0941</span>
      </li>
      <li class="contacts__item">
        <svg class="contacts__icon" viewBox="0 0 16 16" aria-hidden="true"><rect x="1" y="3" width="14" height="10" rx="1" fill="none" stroke="#fff" stroke-width="1.6"/><path d="M1.5 3.8 8 9l6.5-5.2" fill="none" stroke="#fff" stroke-width="1.6"/></svg>
        <span>service@crestfieldautomotive.example</span>
      </li>
      <li class="contacts__item">
        <svg class="contacts__icon" viewBox="0 0 16 16" aria-hidden="true"><circle cx="8" cy="8" r="6.5" fill="none" stroke="#fff" stroke-width="1.4"/><ellipse cx="8" cy="8" rx="2.8" ry="6.5" fill="none" stroke="#fff" stroke-width="1.2"/><path d="M1.5 8h13" stroke="#fff" stroke-width="1.2"/></svg>
        <span>crestfieldautomotive.example</span>
      </li>
    </ul>
  </section>

</main>
</body>
</html>
```